1 Cup Pod - Regular and Decaf

I am looking for 2 package designs. When you open the uploaded file it show one for regular and one for decaf. The size is also on the example template. Both products with still be named Café Brisa, only things we are looking for is new colors and design of package. you can use up to 4 colors at this time.

We are open to all types of ideas and colors. the only thins is the regular and decaf must be different colors.

Requirements
Must have
• Must use the exact information used on front and back of both package design from the example template. The only thing is to add, 75702 next to where it says Tyler, TX

```html
<!DOCTYPE html>
<html lang="en">
<head>
<meta charset="utf-8">
<title>Café Brisa — Single-Cup Pod Packaging</title>
<link href="https://fonts.googleapis.com/css2?family=Tinos:wght@400;700&display=swap" rel="stylesheet">
<style>
  :root{
    --stage-light:#7d5742;
    --stage-dark:#3f2819;
    --espresso:#3d2317;
    --bean-dark:#5a3826;
    --latte:#b38a64;
    --gold:#f2c037;
    --cream:#f4e6cf;
    --white:#ffffff;
  }
  html,body{margin:0;padding:0;overflow:hidden;}
  body{width:1200px;height:1000px;}
  .canvas{
    position:relative;width:1200px;height:1000px;overflow:hidden;
    background:radial-gradient(ellipse at 50% 50%,var(--stage-light) 0%,var(--stage-dark) 95%);
    font-family:"Tinos","Times New Roman",serif;
  }
  .package{
    position:absolute;width:917px;height:458px;
    box-shadow:0 4px 14px rgba(0,0,0,.45);
    overflow:hidden;
  }
  .package--regular{left:35px;top:32px;}
  .package--decaf{left:240px;top:512px;}
  .bean-field{
    position:absolute;inset:0;
    background:
      radial-gradient(circle at 20% 30%,rgba(162,122,88,.55) 0,transparent 40%),
      radial-gradient(circle at 75% 70%,rgba(162,122,88,.5) 0,transparent 45%),
      linear-gradient(135deg,var(--bean-dark),#7a5138 50%,var(--bean-dark));
  }
  .badge{position:absolute;width:280px;}
  .package--regular .badge{left:94px;top:36px;height:400px;}
  .package--decaf .badge{left:96px;top:46px;height:410px;}
  .badge svg{position:absolute;inset:0;width:100%;height:100%;}
  .badge__content{position:absolute;inset:0;text-align:center;}
  .brand-name{
    position:absolute;left:0;right:0;margin:0;
    font-weight:400;font-size:72px;line-height:62px;letter-spacing:0;
    color:var(--gold);
  }
  .brand-name__first{display:block;}
  .package--regular .brand-name{top:150px;}
  .package--regular .brand-name__first{color:var(--white);}
  .package--decaf .brand-name{top:132px;}
  .package--decaf .brand-name__first{color:var(--espresso);}
  .product-info{
    position:absolute;left:0;right:0;margin:0;
    font-size:15px;line-height:19px;
  }
  .package--regular .product-info{top:272px;color:var(--white);}
  .package--decaf .product-info{top:302px;color:var(--espresso);}
  .variant{
    display:block;margin-top:7px;font-weight:700;font-size:19px;color:var(--gold);
    letter-spacing:.5px;
  }
  .directions{
    position:absolute;left:569px;top:108px;width:236px;height:260px;box-sizing:border-box;
    border:3px solid var(--gold);border-radius:22px;
    text-align:center;font-size:14.5px;line-height:17.5px;padding-top:20px;
  }
  .package--regular .directions{background:var(--espresso);color:var(--cream);}
  .package--decaf .directions{background:var(--latte);color:var(--espresso);}
  .directions__title{font-weight:700;display:block;}
  .divider{
    display:block;width:150px;height:2px;margin:38px auto 16px;background:var(--gold);
  }
  .maker{font-weight:700;font-size:15px;line-height:19px;color:var(--gold);}
</style>
</head>
<body>
<div class="canvas">

  <section class="package package--regular">
    <div class="bean-field" role="img" aria-label="Background pattern of roasted coffee beans"></div>
    <div class="badge">
      <svg viewBox="0 0 280 400" preserveAspectRatio="none">
        <path d="M45,14 Q140,-4 235,14 Q238,40 272,48 L272,352 Q238,360 235,386 Q140,404 45,386 Q42,360 8,352 L8,48 Q42,40 45,14 Z" fill="var(--gold)"/>
        <path d="M50,21 Q140,4 230,21 Q233,46 264,54 L264,346 Q233,354 230,379 Q140,396 50,379 Q47,354 16,346 L16,54 Q47,46 50,21 Z" fill="var(--espresso)" stroke="var(--cream)" stroke-width="1.5"/>
      </svg>
      <div class="badge__content">
        <h1 class="brand-name"><span class="brand-name__first">CAFÉ</span>BRISA</h1>
        <p class="product-info">Single-Cup Coffee Pod<br>Colombian 7g<span class="variant">REGULAR</span></p>
      </div>
    </div>
    <div class="directions">
      <span class="directions__title">DIRECTIONS:</span>
      Carefully open package.<br>DO NOT OPEN FILTER PACK<br>Place single-cup coffee pod<br>in brew basket or funnel.<br>Follow the directions<br>on you coffee maker.
      <span class="divider"></span>
      <div class="maker">QUILLANE &amp; SONS<br>Corvane, Texas, 00000</div>
    </div>
  </section>

  <section class="package package--decaf">
    <div class="bean-field" role="img" aria-label="Background pattern of roasted coffee beans"></div>
    <div class="badge">
      <svg viewBox="0 0 280 400" preserveAspectRatio="none">
        <path d="M45,14 Q140,-4 235,14 Q238,40 272,48 L272,352 Q238,360 235,386 Q140,404 45,386 Q42,360 8,352 L8,48 Q42,40 45,14 Z" fill="var(--gold)"/>
        <path d="M50,21 Q140,4 230,21 Q233,46 264,54 L264,346 Q233,354 230,379 Q140,396 50,379 Q47,354 16,346 L16,54 Q47,46 50,21 Z" fill="var(--latte)" stroke="var(--cream)" stroke-width="1.5"/>
      </svg>
      <div class="badge__content">
        <h1 class="brand-name"><span class="brand-name__first">CAFÉ</span>BRISA</h1>
        <p class="product-info">Single-Cup Coffee Pod<br>Colombian 7g<span class="variant">DECAFFEINATED</span></p>
      </div>
    </div>
    <div class="directions">
      <span class="directions__title">DIRECTIONS:</span>
      Carefully open package.<br>DO NOT OPEN FILTER PACK<br>Place single-cup coffee pod<br>in brew basket or funnel.<br>Follow the directions<br>on you coffee maker.
      <span class="divider"></span>
      <div class="maker">QUILLANE &amp; SONS<br>Corvane, Texas, 00000</div>
    </div>
  </section>

</div>
</body>
</html>
```